Veldon Tracing, Inc. - Stationary Project
Business Cards and Stationary for Missing Person Consultants
Professional
Luke Hammond
Search Coordinator
718 West Marlow Avenue
Suite #263
Orlando, FL 32806
lhammond@veldontracing-demo.org
www.VeldonTracing-demo.org
Our organization is called upon
when someone disappears. We¹d like to have a professional business card that
is very eye-catching and people will notice. Please use the red, black and
gray colors in the logo to make a great looking business card, letterhead
and envelope. We look forward to seeing your designs.
We'd like to see a clever use of the logo on the back of the card in bigger format.
This is our logo in AI format.

```html
<!DOCTYPE html>
<html lang="en">
<head>
<meta charset="utf-8">
<title>Veldon Tracing – Stationery Concepts</title>
<link href="https://fonts.googleapis.com/css2?family=Roboto:wght@400;700&family=Roboto+Condensed:wght@700&display=swap" rel="stylesheet">
<style>
:root{
  --bg-top:#16304d;
  --bg-bottom:#02060c;
  --red:#c0202a;
  --red-dark:#5e0c10;
  --ink:#2a2a2a;
  --gray:#8a8d92;
  --paper:#ffffff;
  --label:#6f8299;
  --flap:#1c1f24;
}
*{margin:0;padding:0;box-sizing:border-box}
html,body{width:1200px;height:473px;overflow:hidden}
body{font-family:"Roboto",sans-serif;background:var(--bg-bottom)}
.canvas{position:relative;width:1200px;height:473px;overflow:hidden;
  background:radial-gradient(ellipse 70% 60% at 30% 15%,var(--bg-top),var(--bg-bottom) 80%)}
.brand{position:absolute;left:66px;top:68px;display:flex;align-items:center;gap:12px}
.brand-dot{width:52px;height:52px;border-radius:50%;background:var(--red);border:3px solid #d8d8d8}
.brand-name{font-family:"Roboto Condensed",sans-serif;font-weight:700;color:#fff;font-size:30px;line-height:1;letter-spacing:1px}
.brand-sub{position:absolute;left:132px;top:140px;color:var(--label);font-size:9px}
.item{position:absolute}
.label{position:absolute;left:0;right:0;text-align:center;color:var(--label);font-size:6px;bottom:-13px}
.card{width:190px;height:103px;border-radius:4px;background:var(--paper);box-shadow:0 2px 6px rgba(0,0,0,.5)}
.card-red{background:radial-gradient(circle at 50% 50%,var(--red),var(--red-dark))}
.mini-name{font-family:"Roboto Condensed",sans-serif;font-weight:700;font-size:9px;color:var(--ink);letter-spacing:.5px}
.mini-mark{display:flex;align-items:center;gap:4px}
.mini-dot{width:14px;height:14px;border-radius:50%;background:var(--red)}
.tiny{font-size:5px;color:var(--ink);line-height:1.5}
.person{font-size:8px;font-weight:700;color:var(--red)}
.role{font-size:5px;color:var(--gray)}
.card-front{padding:12px;display:flex;justify-content:space-between}
.card-front .col{display:flex;flex-direction:column;justify-content:space-between}
.card-back{display:flex;flex-direction:column;align-items:center;justify-content:center;gap:6px}
.card-back .mini-name{font-size:12px}
.card-red .mini-name{color:#fff}
.card-red .mini-dot{background:#fff}
.card-back .mini-dot{width:22px;height:22px}
.letterhead{width:317px;height:432px;background:var(--paper);box-shadow:0 3px 10px rgba(0,0,0,.6);padding:22px 24px}
.lh-top{display:flex;justify-content:space-between;align-items:flex-start}
.lh-top .mini-name{font-size:13px}
.lh-top .mini-dot{width:24px;height:24px}
.lh-faint{position:absolute;left:98px;top:150px;width:120px;height:120px;border-radius:50%;border:14px solid #efefef}
.envelope{position:absolute;width:300px;height:150px;background:var(--paper);box-shadow:0 3px 10px rgba(0,0,0,.6);overflow:hidden}
.env-back{left:10px;top:0}
.env-mid{left:40px;top:34px}
.env-front{left:96px;top:110px;height:172px}
.env-front .face{height:100px;background:radial-gradient(ellipse at 50% 30%,var(--red),var(--red-dark))}
.env-front .foot{padding:10px 14px}
.env-faint{position:absolute;right:24px;bottom:14px;width:70px;height:70px;border-radius:50%;border:8px solid #efefef}
.env-seal{position:absolute;left:50%;width:26px;height:26px;margin-left:-13px;border-radius:50%;background:var(--red);border:2px solid #ddd}
</style>
</head>
<body>
<div class="canvas">

  <div class="brand">
    <span class="brand-dot"></span>
    <span class="brand-name">VELDON TRACING</span>
  </div>
  <p class="brand-sub">Stationery Concepts</p>

  <!-- business cards -->
  <div class="item card card-front" style="left:43px;top:190px">
    <div class="col">
      <div class="mini-mark"><span class="mini-dot"></span><span class="mini-name">VELDON TRACING</span></div>
      <div class="tiny">718 West Marlow Avenue<br>Suite #263<br>Orlando, FL 32806</div>
    </div>
    <div class="col" style="text-align:right">
      <div><div class="person">Luke Hammond</div><div class="role">Search Coordinator</div></div>
      <div class="tiny">407 555 0148<br>407 555 0192<br>lhammond@veldontracing-demo.org</div>
    </div>
    <span class="label">Business card front, option one</span>
  </div>

  <div class="item card card-front" style="left:242px;top:190px">
    <div class="col">
      <div class="tiny">718 West Marlow Avenue<br>Suite #263<br>Orlando, FL 32806</div>
      <div class="tiny">407 555 0148<br>lhammond@veldontracing-demo.org</div>
    </div>
    <div class="col" style="text-align:right;align-items:flex-end">
      <span class="mini-dot" style="width:22px;height:22px"></span>
      <div><div class="person">Luke Hammond</div><div class="role">Search Coordinator</div></div>
    </div>
    <span class="label">Business card front, option two</span>
  </div>

  <div class="item card card-back" style="left:43px;top:324px">
    <div class="mini-mark"><span class="mini-dot"></span><span class="mini-name">VELDON TRACING</span></div>
    <div class="tiny">www.VeldonTracing-demo.org</div>
    <span class="label">Card back, white</span>
  </div>

  <div class="item card card-back card-red" style="left:242px;top:324px">
    <div class="mini-mark"><span class="mini-dot"></span><span class="mini-name">VELDON TRACING</span></div>
    <span class="label">Card back, red</span>
  </div>

  <!-- letterhead -->
  <div class="item letterhead" style="left:439px;top:24px">
    <div class="lh-top">
      <div class="mini-mark"><span class="mini-dot"></span><span class="mini-name">VELDON TRACING</span></div>
      <div class="tiny">718 West Marlow Avenue<br>Suite #263<br>Orlando, FL 32806<br>407 555 0148<br>www.VeldonTracing-demo.org</div>
    </div>
    <span class="lh-faint"></span>
    <span class="label">Letterhead</span>
  </div>

  <!-- envelopes -->
  <div class="item" style="left:780px;top:115px;width:400px;height:320px">
    <div class="envelope env-back">
      <svg width="300" height="80" viewBox="0 0 300 80" style="position:absolute;top:0;left:0">
        <polygon points="0,0 300,0 150,80" fill="var(--flap)"/>
      </svg>
      <span class="env-seal" style="top:48px"></span>
    </div>
    <div class="envelope env-mid">
      <svg width="300" height="70" viewBox="0 0 300 70" style="position:absolute;top:0;left:0">
        <polyline points="0,0 150,70 300,0" fill="none" stroke="#dcdcdc" stroke-width="1.5"/>
      </svg>
      <span class="env-seal" style="top:54px"></span>
    </div>
    <div class="envelope env-front">
      <div class="face"></div>
      <div class="foot">
        <div class="mini-mark"><span class="mini-dot"></span><span class="mini-name">VELDON TRACING</span></div>
        <div class="tiny">718 West Marlow Avenue, Suite #263<br>Orlando, FL 32806</div>
      </div>
      <span class="env-faint"></span>
    </div>
    <span class="label" style="bottom:-6px;left:96px;width:300px">Envelopes</span>
  </div>

</div>
</body>
</html>
```